Company or website name
- FreedFromQuietHarmToday.com
- Links to the website
- Nora Joyce Palmer, mental health professional,new book,"Hushed Walls, Yet Open Doors Await" - Brought to the point of the unspoken-helping people get out and stay out of emotionally abusive relationships-www.FreedFromQuietHarmToday.com
- Other Facts

```html
<!DOCTYPE html>
<html lang="en">
<head>
<meta charset="utf-8">
<title>FreedFromQuietHarmToday.com – Banner</title>
<link rel="stylesheet" href="https://fonts.googleapis.com/css2?family=Cinzel:wght@400;600&display=swap">
<style>
  :root {
    --page: #ffffff;
    --band: #000000;
    --band-soft: #1a1a1a;
    --gloss: #3a3a3a;
    --fence-dark: #0b0b0b;
    --fence-mid: #4a4a4a;
    --ink: #ffffff;
  }
  * { margin: 0; padding: 0; box-sizing: border-box; }
  html, body {
    width: 1200px;
    height: 341px;
    overflow: hidden;
    background: var(--page);
  }
  .canvas {
    position: relative;
    width: 1200px;
    height: 341px;
    background: var(--page);
  }
  .banner {
    position: absolute;
    left: 57px;
    top: 50px;
    width: 1079px;
    height: 228px;
    background: var(--band);
    overflow: hidden;
  }
  .banner__gloss {
    position: absolute;
    inset: 0;
    width: 100%;
    height: 100%;
  }
  .banner__fence {
    position: absolute;
    left: 0;
    top: 0;
    width: 493px;
    height: 228px;
    background:
      radial-gradient(ellipse at 55% 50%, rgba(0,0,0,0.85) 0%, rgba(0,0,0,0.55) 30%, rgba(0,0,0,0) 60%),
      linear-gradient(90deg, var(--fence-mid) 0%, var(--fence-dark) 45%, var(--fence-mid) 75%, var(--fence-dark) 100%);
  }
  .site-name {
    position: absolute;
    left: 110px;
    top: 48px;
    width: 240px;
    font-family: "Cinzel", serif;
    font-weight: 600;
    font-size: 33px;
    line-height: 37px;
    color: var(--ink);
    text-align: center;
    text-shadow: 0 0 6px rgba(0,0,0,0.9);
  }
  .author-name {
    position: absolute;
    left: 800px;
    top: 164px;
    width: 270px;
    font-family: "Cinzel", serif;
    font-weight: 400;
    font-size: 17px;
    line-height: 26px;
    letter-spacing: 4px;
    color: var(--ink);
    text-align: center;
  }
</style>
</head>
<body>
  <main class="canvas">
    <section class="banner">
      <svg class="banner__gloss" viewBox="0 0 1079 228" preserveAspectRatio="none" aria-hidden="true">
        <defs>
          <linearGradient id="gloss-fade" x1="0" y1="0" x2="0" y2="1">
            <stop offset="0" stop-color="#2a2a2a"/>
            <stop offset="1" stop-color="#4a4a4a"/>
          </linearGradient>
        </defs>
        <path d="M0 0 H1079 V100 C800 118 500 128 0 140 Z" fill="url(#gloss-fade)" opacity="0.85"/>
      </svg>
      <div class="banner__fence" role="img" aria-label="Chain-link fence torn open in the middle, in silver on black"></div>
      <h1 class="site-name">Freed<br>From Quiet<br>Harm<br>Today.com</h1>
      <p class="author-name">Nora Joyce<br>Palmer</p>
    </section>
  </main>
</body>
</html>
```